Business Card Design

Quorvel Software Limited develops and sells venue and event management software called Quorvel Stagehand, which is available in the cloud or on-premise. The company was established in 1986. Most of our customers are performing arts venues, museums and festivals. Our existing design is a bit dull. We need to convey that we are both innovative and reliable.
Not all our people show their mobile phone numbers on their cards, so the design needs to work land line and mobile or land line only.

Industry/Entity Type

Software

Contact Information for Business Card

Helen Trasko
Director
Quorvel Software Limited
42B Milbrook Lane, Epsom, Surrey, KT19 4DN
Telephone: +44 (0)1372 640913
Mobile: +44 (0)7945 216804
Email: htrasko@quorvel.net
Web: www.quorvel.net

```html
<!DOCTYPE html>
<html lang="en">
<head>
<meta charset="utf-8">
<title>Quorvel Business Card</title>
<link href="https://fonts.googleapis.com/css2?family=Open+Sans:wght@400;600;700&display=swap" rel="stylesheet">
<style>
  :root {
    --bg: #a9a9ad;
    --card: #ffffff;
    --brand: #2f5f85;
    --band-dark: #1b6aa5;
    --band-light: #5a9bc6;
    --accent: #3c8fc8;
    --ink-grey: #8a8a8a;
    --rule: #c8c8c8;
  }
  * { margin: 0; padding: 0; box-sizing: border-box; }
  html, body { width: 1200px; height: 863px; overflow: hidden; }
  body {
    background: var(--bg);
    font-family: "Open Sans", Arial, sans-serif;
    position: relative;
  }
  .card {
    position: absolute;
    width: 620px;
    height: 354px;
    background: var(--card);
    box-shadow: 0 10px 24px rgba(0,0,0,0.25);
    overflow: hidden;
  }
  .card--front { left: 110px; top: 45px; }
  .card--back { left: 470px; top: 460px; }

  .band {
    position: absolute;
    left: 0; right: 0; bottom: 0;
    height: 62px;
    background: linear-gradient(90deg, var(--band-dark) 0%, var(--band-dark) 45%, var(--band-light) 100%);
  }
  .band::before {
    content: "";
    position: absolute;
    left: 0; right: 0; top: -9px;
    height: 2px;
    background: var(--rule);
  }
  .band__text {
    position: absolute;
    left: 40px; top: 50%;
    transform: translateY(-50%);
    color: #fff;
    font-size: 15px;
    letter-spacing: 2.5px;
  }

  .brand {
    position: absolute;
    display: flex;
    align-items: center;
    gap: 12px;
  }
  .brand__mark {
    width: 34px; height: 34px;
    background: var(--brand);
  }
  .brand__name {
    color: var(--brand);
    font-weight: 700;
    font-size: 44px;
    letter-spacing: 1px;
    line-height: 1;
  }
  .card--front .brand { left: 175px; top: 105px; }
  .brand__web {
    position: absolute;
    left: 221px; top: 158px;
    color: var(--brand);
    font-size: 13px;
  }

  .card--back .brand { left: 40px; top: 95px; }
  .card--back .brand__name { font-size: 36px; }
  .card--back .brand__mark { width: 28px; height: 28px; }
  .card--back .band__text { left: 70px; font-size: 16px; letter-spacing: 3px; }

  .divider {
    position: absolute;
    left: 0; top: 0;
    width: 620px; height: 292px;
  }

  .contact {
    position: absolute;
    left: 350px; top: 52px;
    color: var(--ink-grey);
  }
  .contact__name { font-size: 24px; font-weight: 600; line-height: 1.1; }
  .contact__role { color: var(--accent); font-size: 14px; margin-bottom: 18px; }
  .contact__address { font-size: 13px; line-height: 1.35; margin-bottom: 12px; max-width: 240px; }
  .contact__line {
    display: flex; align-items: center; gap: 10px;
    font-size: 13.5px; line-height: 1.55;
  }
  .contact__icon { width: 14px; height: 14px; flex: none; }
</style>
</head>
<body>

  <section class="card card--front">
    <div class="brand">
      <span class="brand__mark"></span>
      <span class="brand__name">QUORVEL</span>
    </div>
    <div class="brand__web">www.quorvel.net</div>
    <div class="band">
      <span class="band__text">Venue and Event management software</span>
    </div>
  </section>

  <section class="card card--back">
    <svg class="divider" viewBox="0 0 620 292" aria-hidden="true">
      <line x1="250" y1="292" x2="335" y2="48" stroke="#cfcfcf" stroke-width="1.5"/>
    </svg>
    <div class="brand">
      <span class="brand__mark"></span>
      <span class="brand__name">QUORVEL</span>
    </div>

    <div class="contact">
      <div class="contact__name">Helen Trasko</div>
      <div class="contact__role">Director</div>
      <div class="contact__address">Quorvel Software Limited<br>42B Milbrook Lane, Epsom, Surrey, KT19 4DN</div>
      <div class="contact__line">
        <svg class="contact__icon" viewBox="0 0 14 14"><rect x="3.5" y="1" width="7" height="12" rx="1.2" fill="none" stroke="#3c8fc8" stroke-width="1.4"/><circle cx="7" cy="10.8" r="0.8" fill="#3c8fc8"/></svg>
        <span>+44 (0)7945 216804</span>
      </div>
      <div class="contact__line">
        <svg class="contact__icon" viewBox="0 0 14 14"><path d="M2 5 Q7 1 12 5 L10.5 6.5 L9 5.2 L5 5.2 L3.5 6.5 Z" fill="#3c8fc8"/><rect x="3" y="7.5" width="8" height="5" rx="1" fill="#3c8fc8"/></svg>
        <span>+44 (0)1372 640913</span>
      </div>
      <div class="contact__line">
        <svg class="contact__icon" viewBox="0 0 14 14"><rect x="1.5" y="3" width="11" height="8" rx="1" fill="none" stroke="#3c8fc8" stroke-width="1.4"/><path d="M1.5 3.5 L7 8 L12.5 3.5" fill="none" stroke="#3c8fc8" stroke-width="1.4"/></svg>
        <span>htrasko@quorvel.net</span>
      </div>
    </div>

    <div class="band">
      <span class="band__text">www.quorvel.net</span>
    </div>
  </section>

</body>
</html>
```